Roadward Lane Management Company Website

Modern website Wordpress design using all greyscale photos with a pop of red (such as road closure signs or detour cones) for strategic emphasis. (see brand guide for color codes)
The creative goal is to leverage high-contrast, desaturated imagery to create a clean, professional, and industrial feel. The selective use of red will draw immediate attention to critical elements—such as road hazards, safety equipment, or key messages to ensure the viewer's focus is directed with purpose.

Brand guide, homepage content and logo are attached. Create clean professional user experience to market services to industry professionals.

```html
<!DOCTYPE html>
<html lang="en">
<head>
<meta charset="UTF-8">
<title>Roadward Lane Management Company</title>
<link href="https://fonts.googleapis.com/css2?family=Inter+Tight:ital,wght@0,400;0,500;0,600;0,700;1,600;1,700&display=swap" rel="stylesheet">
<style>
:root{
  --red:#e8202a;
  --red-deep:#7a1014;
  --black:#000000;
  --ink:#111111;
  --quote-ink:#2a1414;
  --white:#ffffff;
  --grey-soft:#ececec;
  --card-shadow:0 4px 16px rgba(0,0,0,.12);
}
*{box-sizing:border-box;margin:0;padding:0}
html,body{width:1200px;height:3900px;overflow:hidden}
body{font-family:"Inter Tight",Arial,sans-serif;color:var(--ink);background:var(--white);position:relative}
.abs{position:absolute}

/* header */
.site-header{position:absolute;top:0;left:0;width:1200px;height:90px}
.brand{position:absolute;left:110px;top:30px;display:flex;align-items:center;gap:8px;font-weight:700;font-size:22px;color:var(--ink)}
.brand-square{width:18px;height:18px;background:var(--red)}
.main-nav{position:absolute;left:407px;top:34px;display:flex;gap:31px;font-size:17px}
.btn-red{position:absolute;background:var(--red);color:var(--white);border-radius:30px;display:flex;align-items:center;justify-content:center;font-weight:500}
.btn-contact{left:972px;top:24px;width:118px;height:42px;font-size:17px}

/* hero */
.hero-art{left:340px;top:100px;width:860px;height:546px;background:linear-gradient(100deg,#ffffff 0%,#f2f2f2 30%,#d8d8d8 65%,#c9c9c9 80%,#e6e6e6 100%)}
.hero-art::after{content:"";position:absolute;left:500px;top:60px;width:160px;height:160px;border-radius:50%;background:radial-gradient(circle,rgba(232,32,42,.55),rgba(232,32,42,0) 70%)}
.hero-title{left:110px;top:170px;font-size:58px;font-weight:700;line-height:60px;letter-spacing:-1px;width:460px}
.btn-hero{left:110px;top:450px;width:166px;height:44px;font-size:19px}

/* hazard band (flat fill) */
.hazard-band{left:0;top:646px;width:1200px;height:130px;background:linear-gradient(90deg,var(--red-deep) 0%,var(--black) 30%,var(--red-deep) 50%,var(--black) 70%,var(--red-deep) 100%)}
.feature-card{position:absolute;top:698px;width:199px;height:178px;background:var(--white);border-radius:6px;box-shadow:var(--card-shadow);text-align:center;font-size:19px;font-weight:500;line-height:25px}
.feature-card svg{display:block;margin:28px auto 14px}

/* quote */
.quote-mark{left:510px;top:890px;font-size:300px;font-weight:700;color:var(--grey-soft);line-height:1;font-family:Georgia,serif}
.quote-text{left:200px;top:1098px;width:800px;text-align:center;font-style:italic;font-weight:700;font-size:52px;line-height:58px;color:var(--quote-ink);letter-spacing:-1px}

/* services grid */
.service{position:absolute;width:240px;text-align:center;font-size:23px;line-height:27px}
.service svg{display:block;margin:0 auto 14px}

/* industries */
.industries{left:0;top:1983px;width:1200px;height:1577px;background:radial-gradient(ellipse 600px 500px at 0% 15%,#3a0808 0%,rgba(0,0,0,0) 100%),radial-gradient(ellipse 500px 600px at 100% 85%,#3a0808 0%,rgba(0,0,0,0) 100%),var(--black)}
.industries-title{left:240px;top:2088px;width:720px;text-align:center;color:var(--white);font-style:italic;font-weight:600;font-size:52px;line-height:62px;letter-spacing:-.5px}
.industry-label{position:absolute;left:110px;width:370px;color:var(--white);font-size:42px;line-height:50px;font-weight:500;letter-spacing:-.5px}
.industry-rule{position:absolute;height:2px;width:370px;background:linear-gradient(90deg,rgba(232,32,42,0),var(--red) 30%,rgba(232,32,42,0))}
.industry-photo{position:absolute;left:591px;width:499px;border-radius:4px;background:linear-gradient(180deg,#d9d9d9 0%,#a0a0a0 50%,#5a5a5a 100%)}

/* footer */
.footer-brand{left:0;top:3635px;width:1200px;display:flex;justify-content:center;align-items:center;gap:8px;font-weight:700;font-size:30px}
.footer-rule{left:83px;top:3743px;width:1034px;height:1px;background:#cfcfcf}
.footer-nav{left:85px;top:3764px;display:flex;gap:40px;font-size:24px}
.partner-badge{left:968px;top:3756px;width:145px;height:44px;background:#1c3c6e;border-radius:4px}
.bottom-band{left:0;top:3835px;width:1200px;height:65px;background:linear-gradient(90deg,var(--red-deep) 0%,var(--black) 30%,var(--red-deep) 50%,var(--black) 70%,var(--red-deep) 100%)}
.legal{left:80px;top:3867px;color:var(--white);font-size:13px}
</style>
</head>
<body>

<header class="site-header">
  <div class="brand"><span class="brand-square"></span>Roadward</div>
  <nav class="main-nav"><span>Home</span><span>About</span><span>Services</span><span>Rentals</span><span>Jobs</span></nav>
  <a class="btn-red btn-contact">Contact Us</a>
</header>

<div class="abs hero-art" role="img" aria-label="Greyscale sketch of a highway with cars and a red stop sign"></div>
<h1 class="abs hero-title">Traffic Control Solutions Engineered For Safety.</h1>
<a class="btn-red btn-hero">Find Out More</a>

<div class="abs hazard-band" role="img" aria-label="Red and black hazard stripe band"></div>

<div class="feature-card" style="left:182px">
  <svg width="48" height="52" viewBox="0 0 48 52"><path d="M24 2 44 10v16c0 13-9 21-20 24C13 47 4 39 4 26V10z" fill="#e8202a"/><path d="M14 26l7 7 13-14" stroke="#fff" stroke-width="5" fill="none"/></svg>
  TxDOT-Compliant<br>&amp; Certified
</div>
<div class="feature-card" style="left:395px">
  <svg width="54" height="52" viewBox="0 0 54 52"><path d="M4 14 38 4l3 10z" fill="#e8202a"/><rect x="4" y="16" width="48" height="32" rx="3" fill="#e8202a"/><rect x="32" y="26" width="22" height="12" fill="#fff"/><circle cx="40" cy="32" r="3" fill="#e8202a"/></svg>
  Cost-Effective &amp;<br>Efficient
</div>
<div class="feature-card" style="left:607px">
  <svg width="52" height="52" viewBox="0 0 52 52"><path d="M12 20a14 14 0 0 1 28 0z" fill="#e8202a"/><rect x="8" y="20" width="36" height="4" fill="#e8202a"/><circle cx="26" cy="29" r="7" fill="#e8202a"/><path d="M6 52v-8c0-6 8-9 20-9s20 3 20 9v8z" fill="#e8202a"/><rect x="22" y="38" width="8" height="14" fill="#fff"/></svg>
  Experienced &amp;<br>Trained Crew
</div>
<div class="feature-card" style="left:820px">
  <svg width="64" height="48" viewBox="0 0 64 48"><path d="M2 16 14 6l14 8 10-4 12 6 12-8v14L40 40 28 32 14 26 2 30z" fill="#e8202a"/><path d="M24 24l8 8M30 20l8 8M36 18l6 6" stroke="#fff" stroke-width="3"/></svg>
  Reliable &amp;<br>Responsive
</div>

<div class="abs quote-mark">&ldquo;</div>
<p class="abs quote-text">Safety isn’t a priority, it is the foundation of everything we do</p>

<div class="service" style="left:139px;top:1322px">
  <svg width="54" height="50" viewBox="0 0 54 50"><path d="M22 2h10l14 40H8z" fill="#e8202a"/><rect x="14" y="14" width="26" height="6" fill="#fff"/><rect x="10" y="28" width="34" height="6" fill="#fff"/><rect x="2" y="42" width="50" height="6" fill="#e8202a"/></svg>
  Flagging &amp; Lane Closures Temporary Traffic
</div>
<div class="service" style="left:485px;top:1322px">
  <svg width="50" height="50" viewBox="0 0 50 50" fill="none" stroke="#e8202a" stroke-width="5"><path d="M17 17V10a7 7 0 1 0-7 7h30a7 7 0 1 0-7-7v30a7 7 0 1 0 7-7H10a7 7 0 1 0 7 7z"/></svg>
  Control Plans<br>(TTCPs)
</div>
<div class="service" style="left:818px;top:1322px">
  <svg width="60" height="50" viewBox="0 0 60 50"><rect x="2" y="8" width="56" height="18" fill="#e8202a"/><path d="M12 8 4 26M26 8l-8 18M40 8l-8 18M54 8l-8 18" stroke="#fff" stroke-width="4"/><rect x="8" y="26" width="6" height="20" fill="#e8202a"/><rect x="46" y="26" width="6" height="20" fill="#e8202a"/><rect x="8" y="36" width="44" height="5" fill="#e8202a"/></svg>
  Signage &amp;<br>Barricades<br>Crash<br>Attenuators &amp;
</div>
<div class="service" style="left:139px;top:1546px">
  <svg width="60" height="48" viewBox="0 0 60 48" fill="none" stroke="#e8202a" stroke-width="4"><rect x="2" y="4" width="32" height="30" rx="3"/><path d="M34 14h14l10 12v8H34z"/><circle cx="14" cy="38" r="6" fill="#fff"/><circle cx="46" cy="38" r="6" fill="#fff"/></svg>
  Truck Mounted<br>Attenuators<br>(TMAs)
</div>
<div class="service" style="left:485px;top:1536px">
  <svg width="52" height="52" viewBox="0 0 52 52"><path d="M18 2h6l-2 12h-8zM28 2h6l4 12h-8z" fill="#e8202a"/><rect x="2" y="14" width="48" height="6" fill="#e8202a"/><path d="M12 20h10l-4 32H6zM30 20h10l6 32H34z" fill="#e8202a"/></svg>
  Heavy Highway<br>Traffic Control
</div>
<div class="service" style="left:818px;top:1536px">
  <svg width="40" height="52" viewBox="0 0 40 52" fill="none" stroke="#e8202a" stroke-width="4"><path d="M8 52V4M8 26l22-20M22 4h10v10"/></svg>
  Roadway<br>Detours &amp; Lane<br>Shifts
</div>
<div class="service" style="left:139px;top:1738px">
  <svg width="58" height="50" viewBox="0 0 58 50" fill="none" stroke="#e8202a" stroke-width="3"><path d="M4 4h50v32H24l-10 10v-10H4z"/><path d="M14 14h30M14 21h30M14 28h22"/></svg>
  Work Zone Safety<br>Consulting for<br>Compliance
</div>
<div class="service" style="left:485px;top:1738px">
  <svg width="48" height="52" viewBox="0 0 48 52" fill="none" stroke="#e8202a" stroke-width="3"><rect x="8" y="2" width="36" height="44"/><path d="M8 46a4 4 0 0 0 0 4h36M4 6v42"/><circle cx="26" cy="16" r="6"/><path d="M16 32h20M18 38h16"/></svg>
  with TxDOT and<br>OSHA<br>regulations
</div>
<div class="service" style="left:818px;top:1738px">
  <svg width="40" height="52" viewBox="0 0 40 52" fill="none" stroke="#e8202a" stroke-width="3"><rect x="10" y="2" width="20" height="44" rx="4"/><circle cx="20" cy="12" r="4" fill="#e8202a"/><circle cx="20" cy="24" r="4" fill="#e8202a"/><circle cx="20" cy="36" r="4" fill="#e8202a"/><path d="M2 10h8M30 10h8M2 22h8M30 22h8M20 46v6"/></svg>
  Event Traffic &amp;<br>Crowd Control
</div>

<section class="abs industries"></section>
<h2 class="abs industries-title">Serving Texas Industry to Ensure Safety, Compliance, and Efficient Traffic Flow</h2>

<div class="industry-label" style="top:2435px">Road construction, maintenance, &amp; Detours</div>
<div class="industry-rule" style="left:130px;top:2630px"></div>
<div class="industry-photo" style="top:2438px;height:194px;background:linear-gradient(180deg,#f0f0f0 0%,#bdbdbd 55%,#6e6e6e 100%)" role="img" aria-label="Greyscale photo of a road work warning sign against cloudy sky"></div>

<div class="industry-label" style="top:2695px">Municipal &amp; State projects</div>
<div class="industry-rule" style="left:110px;top:2888px"></div>
<div class="industry-photo" style="top:2686px;height:212px;background:linear-gradient(180deg,#5a5a5a 0%,#8c8c8c 45%,#b5b5b5 100%)" role="img" aria-label="Greyscale photo of heavy trucks on a highway"></div>

<div class="industry-label" style="top:2955px">Private Sector &amp; Commercial Contractors</div>
<div class="industry-rule" style="left:120px;top:3167px"></div>
<div class="industry-photo" style="top:2960px;height:210px;background:linear-gradient(180deg,#cfcfcf 0%,#8a8a8a 50%,#4e4e4e 100%)" role="img" aria-label="Greyscale photo of construction equipment on a graded roadway"></div>

<div class="industry-label" style="top:3228px;width:300px">Oil, Gas, Wind, Solar, &amp; Manufacturing</div>
<div class="industry-photo" style="top:3237px;height:211px;background:linear-gradient(90deg,#e0e0e0 0%,#9a9a9a 40%,#4a4a4a 100%)" role="img" aria-label="Greyscale photo of an industrial plant with a wind turbine"></div>

<div class="abs footer-brand"><span class="brand-square"></span>Roadward</div>
<div class="abs footer-rule"></div>
<nav class="abs footer-nav"><span>Home</span><span>About</span><span>Services</span><span>Rentals</span><span>Jobs</span></nav>
<div class="abs partner-badge"></div>

<div class="abs bottom-band" role="img" aria-label="Red and black hazard stripe band"></div>
<div class="abs legal">Privacy Stement - Terms &amp; Conditons</div>

</body>
</html>
```